Website design for commercial and residential security company

we're looking to see some new designs for an established company with no website.

homepage and one inner page

here is a link to the homepage content, sitemap, logo and more.
https://files.brontavel.net/share/7QxmPzLrTw2vNkdJhYcsa9eFgbUoiVwRn?view=open

call to action should be Request A Quote

if you have any questions please send them to us asap

thank you

1 page

Sans Serif

```html
<!DOCTYPE html>
<html lang="en">
<head>
<meta charset="utf-8">
<title>Beacon Ridge Security Solutions</title>
<link href="https://fonts.googleapis.com/css2?family=Poppins:wght@400;500;600;700;800&family=Open+Sans:wght@400;600&display=swap" rel="stylesheet">
<style>
:root{
  --gold:#cfae3c;
  --gold-soft:#d8bf62;
  --navy:#1f2757;
  --ink:#161616;
  --text:#666;
  --sage:#e8ede1;
  --white:#fff;
  --line:#e4e4e4;
}
*{margin:0;padding:0;box-sizing:border-box}
html,body{width:1200px;height:5000px;overflow:hidden;background:var(--white)}
body{font-family:"Open Sans",sans-serif;color:var(--text)}
.page{position:relative;width:1200px;height:5000px;overflow:hidden}
.abs{position:absolute}
.heading-font{font-family:"Poppins",sans-serif}

/* header */
.topbar{left:440px;top:0;width:736px;height:36px;background:var(--gold);color:#fff;font-size:12px;display:flex;align-items:center;gap:54px;padding-left:60px}
.topbar .phone{margin-left:auto;margin-right:22px}
.navbar{left:390px;top:36px;width:786px;height:100px;background:var(--ink);clip-path:polygon(0 0,100% 0,100% 100%,60px 100%)}
.nav{left:430px;top:64px;display:flex;gap:106px;font-family:"Poppins",sans-serif;font-size:12px;color:#fff}
.apply{left:982px;top:55px;width:142px;height:40px;border:1px solid var(--gold);border-radius:4px;color:#fff;font-family:"Poppins",sans-serif;font-size:11px;display:flex;align-items:center;justify-content:center;gap:6px}
.brand{left:30px;top:34px;display:flex;align-items:center;gap:10px}
.brand .dot{width:18px;height:18px;border-radius:50%;background:var(--gold)}
.brand .name{font-family:"Poppins",sans-serif;font-weight:700;font-size:21px;line-height:1.05;color:var(--navy);letter-spacing:.5px}

/* hero */
.hero{left:23px;top:140px;width:1153px;height:628px;background:linear-gradient(100deg,#8e8e8c 0%,#5e5e5c 45%,#4d4d4b 100%)}
.hero-art{left:60px;top:160px;width:300px;height:560px;border-radius:40px;background:linear-gradient(180deg,#c9c9c6,#3a3a38)}
.hero-kicker{left:347px;top:366px;font-family:"Poppins",sans-serif;font-weight:600;font-size:16px;color:#fff;text-decoration:underline}
.hero-title{left:347px;top:400px;font-family:"Poppins",sans-serif;font-weight:700;font-size:34px;line-height:50px;color:#fff;text-decoration:underline}
.hero-btn{left:347px;top:548px;width:205px;height:38px;border:2px solid var(--gold);border-radius:20px;color:#fff;font-size:11px;display:flex;align-items:center;padding-left:22px}
.hero-btn .c{position:absolute;right:4px;top:4px;width:26px;height:26px;border-radius:50%;border:1px solid var(--gold);color:var(--gold);font-size:12px;display:flex;align-items:center;justify-content:center}
.social{left:103px;width:26px;height:26px;border:1px solid #ddd;background:rgba(255,255,255,.08)}
.social::after{content:"";position:absolute;left:8px;top:8px;width:8px;height:8px;background:#fff}
.scroll{left:1070px;top:430px;writing-mode:vertical-rl;font-size:9px;color:#eee;letter-spacing:1px}
.scroll::before{content:"";display:inline-block;width:1px;height:60px;background:#eee;margin-bottom:8px}
.dots{left:100px;top:716px;display:flex;gap:13px}
.dots i{width:14px;height:14px;border-radius:50%;background:#fff;display:block}
.dots i.on{background:var(--gold)}
.arrow{top:708px;width:32px;height:32px;border-radius:50%;border:2px solid var(--gold);color:var(--gold);display:flex;align-items:center;justify-content:center;font-size:14px}

/* features */
.feature{top:746px;width:170px;text-align:center}
.feature .circ{width:74px;height:74px;border-radius:50%;background:var(--gold);margin:0 auto 18px;display:flex;align-items:center;justify-content:center}
.feature p{font-family:"Poppins",sans-serif;font-size:19px;color:#333}

/* section titles */
.label{width:1200px;text-align:center;font-family:"Poppins",sans-serif;font-weight:600;font-size:13px;color:var(--navy);text-decoration:underline}
.title{width:1200px;text-align:center;font-family:"Poppins",sans-serif;font-weight:800;font-size:32px;line-height:32px;color:var(--navy);text-decoration:underline}

/* about */
.about-box{left:170px;top:1077px;width:414px;height:295px;background:var(--ink);color:#fff;font-size:11.3px;line-height:19px;padding:26px 22px;text-align:justify}
.about-box p{margin-bottom:19px}
.btn-out{border:2px solid #fff;border-radius:3px;color:#fff;font-family:"Poppins",sans-serif;font-size:11px;display:inline-flex;align-items:center;justify-content:center;gap:6px}
.about-photo{left:582px;top:1063px;width:462px;height:320px;border:3px solid var(--gold);border-radius:10px;background:linear-gradient(120deg,#f3f3f1,#d9dad6 60%,#b8b9b4)}
.mvg{left:155px;top:1401px;width:887px;height:205px;border:3px solid var(--gold-soft);border-radius:16px;border-top-color:#f0e4b8}
.mvg-item{top:1411px;width:280px;text-align:center}
.mvg-item .ring{width:80px;height:80px;border-radius:50%;border:2px solid var(--gold);margin:0 auto 18px;display:flex;align-items:center;justify-content:center}
.mvg-item h3{font-family:"Poppins",sans-serif;font-size:21px;color:var(--navy);margin-bottom:14px}
.mvg-item p{font-size:11.3px;line-height:19px;color:#777}
.btn-gold{border:2px solid var(--gold);border-radius:3px;color:var(--gold);font-family:"Poppins",sans-serif;font-size:11px;display:flex;align-items:center;justify-content:center;gap:6px;background:#fff}

/* services */
.card{width:281px;height:374px;background:#fff;text-align:center}
.card .ph{margin:8px auto 0;width:227px;height:150px}
.card h3{font-family:"Poppins",sans-serif;font-weight:600;font-size:17px;color:var(--ink);margin:10px auto 14px;display:inline-block;border-bottom:2px solid var(--navy);padding:0 14px 2px}
.card p{font-size:11.3px;line-height:19.5px;color:#777;padding:0 15px}
.card .more{margin-top:20px;font-family:"Poppins",sans-serif;font-size:11px;color:var(--gold)}

/* industries */
.ind{width:281px;height:393px;border:2px solid var(--gold)}
.ind .ph{position:absolute;left:17px;top:0;width:245px;height:250px}
.ind .cap{position:absolute;left:6px;top:240px;width:265px;height:148px;background:var(--ink);border-radius:8px;color:#fff;text-align:center;padding:12px 16px}
.ind .cap h3{font-family:"Poppins",sans-serif;font-size:17px;margin-bottom:10px;text-decoration:underline}
.ind .cap p{font-size:11.5px;line-height:19.5px}

/* cta */
.cta{left:23px;top:3624px;width:1153px;height:353px;background:linear-gradient(135deg,#8f908d,#4f504d)}
.cta-gold{left:23px;top:3624px;width:1153px;height:353px;background:var(--gold-soft);clip-path:polygon(0 0,52% 0,83% 100%,0 100%)}
.cta h2{}
.cta-title{left:254px;top:3678px;font-family:"Poppins",sans-serif;font-weight:700;font-size:21px;line-height:24px;color:var(--ink)}
.cta-text{left:254px;top:3740px;width:338px;font-size:11.3px;line-height:19.5px;color:#333;text-align:justify}
.cta-btn{left:345px;top:3884px;width:155px;height:36px;border:1px solid #b58f1e;color:#444;font-size:11px;line-height:13px;text-align:center;padding-top:5px}

/* testimonial */
.testi{left:171px;top:4161px;width:861px;height:370px;background:#fff;box-shadow:0 4px 18px rgba(0,0,0,.14)}
.testi-brand{left:220px;top:4236px;display:flex;align-items:center;gap:14px}
.testi-brand .dot{width:36px;height:36px;border-radius:50%;background:var(--gold)}
.testi-brand .name{font-family:"Poppins",sans-serif;font-weight:700;font-size:34px;line-height:1.05;color:var(--navy)}
.quote{left:212px;top:4338px;width:370px;font-size:11.3px;line-height:19.5px;color:#888}
.testi-line{left:212px;top:4450px;width:30px;height:2px;background:#3a6fd8}
.testi-name{left:212px;top:4466px;font-family:"Poppins",sans-serif;font-size:14px;color:#333}
.testi-role{left:212px;top:4488px;font-size:9px;color:#aaa}
.testi-photo{left:621px;top:4210px;width:388px;height:310px;background:linear-gradient(160deg,#a67a63 0%,#d8d3cc 45%,#eeeeec 100%)}

/* footer */
.footer-col{top:4704px;color:#fff;font-size:11.5px;line-height:19px}
.footer-col h4{font-family:"Poppins",sans-serif;font-size:14px;color:var(--gold-soft);text-decoration:underline;margin-bottom:18px}
.footer-col li{list-style:none;margin-bottom:15px}
.footer-col ul.tight li{margin-bottom:4px}
.copy{left:0;top:4968px;width:1200px;text-align:center;color:#fff;font-size:11px}
</style>
</head>
<body>
<div class="page">

  <!-- header -->
  <div class="abs topbar"><span>&#9679; 48 Harlow Lane Dover, NH 03820</span><span>&#9993; contact@beaconridgesecure.com</span><span class="phone">&#9990; 603-555-0148</span></div>
  <div class="abs navbar"></div>
  <nav class="abs nav"><span>HOME</span><span>ABOUT</span><span>SERVICES</span><span>CONTACT</span></nav>
  <div class="abs apply">APPLY NOW <span>&#10148;</span></div>
  <div class="abs brand"><span class="dot"></span><span class="name">BEACON RIDGE<br>SECURITY SOLUTIONS</span></div>

  <!-- hero -->
  <section class="abs hero" role="img" aria-label="Photo of a security camera shaped like an eye against a grey wall"></section>
  <div class="abs hero-art" role="img" aria-label="Close-up of the eye-shaped security camera"></div>
  <div class="abs hero-kicker">Welcome To Beacon Ridge Security Solutions</div>
  <h1 class="abs hero-title">We Provide Commercial And<br>Residential Security Solution</h1>
  <div class="abs hero-btn">CHECK OUR SERVICES <span class="c">&#8250;</span></div>
  <span class="abs social" style="top:408px"></span>
  <span class="abs social" style="top:450px"></span>
  <span class="abs social" style="top:492px"></span>
  <div class="abs scroll">Scroll Down</div>
  <div class="abs dots"><i></i><i></i><i class="on"></i><i></i><i></i></div>
  <div class="abs arrow" style="left:1015px">&#8249;</div>
  <div class="abs arrow" style="left:1060px">&#8250;</div>

  <!-- features -->
  <div class="abs feature" style="left:336px"><div class="circ"><svg width="34" height="34" viewBox="0 0 24 24" fill="none" stroke="#fff" stroke-width="1.5"><circle cx="12" cy="8" r="5"/><path d="M12 5v6M10 7h3a1 1 0 0 1 0 2h-2a1 1 0 0 0 0 2h3"/><path d="M3 19c3-3 6-3 9-1h5"/></svg></div><p>Affordable Rates</p></div>
  <div class="abs feature" style="left:514px"><div class="circ"><svg width="34" height="34" viewBox="0 0 24 24" fill="none" stroke="#fff" stroke-width="1.5"><circle cx="9" cy="8" r="3.5"/><circle cx="16" cy="9" r="2.5"/><path d="M3 19c0-4 3-6 6-6s6 2 6 6M14 14c3 0 6 1.5 6 5"/></svg></div><p>Expert Staff</p></div>
  <div class="abs feature" style="left:692px"><div class="circ"><svg width="34" height="34" viewBox="0 0 24 24" fill="none" stroke="#fff" stroke-width="1.5"><circle cx="12" cy="9" r="4"/><path d="M6 9a6 6 0 0 1 12 0M5 19c1-4 4-5 7-5s6 1 7 5z"/></svg></div><p>24 x 7 Support</p></div>

  <!-- about -->
  <div class="abs label" style="top:940px">About Us</div>
  <h2 class="abs title" style="top:970px">Welcome To BeaconRidge<br>Security Solutions</h2>
  <div class="abs about-photo" role="img" aria-label="Photo of a white bullet security camera mounted on a wall"></div>
  <div class="abs about-box">
    <p>The graded security measures from Beacon Ridge Security Solutions ensure the safety of both residential and commercial property. We provide a wide range of Residential and Commercial Security Solutions.</p>
    <p>Lorem ipsum dolor sit amet, consectetur adipiscing elit, sed do eiusmod tempor incididunt ut labore et dolore magna aliqua. Ut enim ad minim veniam, quis nostrud exercitation ullamco laboris nisi ut aliquip ex ea commodo consequat.</p>
    <span class="btn-out" style="width:150px;height:38px">KNOW MORE &#10148;</span>
  </div>
  <div class="abs dots" style="left:776px;top:1355px;gap:8px"><i style="width:4px;height:4px;background:#333"></i><i style="width:4px;height:4px;background:#aaa"></i><i style="width:4px;height:4px;background:#aaa"></i><i style="width:4px;height:4px;background:#aaa"></i></div>

  <div class="abs mvg"></div>
  <div class="abs mvg-item" style="left:165px"><div class="ring"><svg width="36" height="36" viewBox="0 0 24 24" fill="none" stroke="#cfae3c" stroke-width="1.4"><path d="M14 4c3-1 6-1 6-1s0 3-1 6l-7 7-5-5z"/><path d="M7 11l-3 1 2 2M13 17l-1 3-2-2M6 18l-2 2"/></svg></div><h3>Mission</h3><p>Lorem ipsum dolor sit amet, consectetur adipiscing elit. Ut elit tellus, luctus nec ullamcorper mattis, pulvinar dapibus leo.</p></div>
  <div class="abs mvg-item" style="left:459px"><div class="ring"><svg width="36" height="36" viewBox="0 0 24 24" fill="none" stroke="#cfae3c" stroke-width="1.4"><path d="M2 12s4-6 10-6 10 6 10 6-4 6-10 6S2 12 2 12z"/><circle cx="12" cy="12" r="3"/></svg></div><h3>Vission</h3><p>Lorem ipsum dolor sit amet, consectetur adipiscing elit. Ut elit tellus, luctus nec ullamcorper mattis, pulvinar dapibus leo.</p></div>
  <div class="abs mvg-item" style="left:753px"><div class="ring"><svg width="36" height="36" viewBox="0 0 24 24" fill="none" stroke="#cfae3c" stroke-width="2.4"><circle cx="12" cy="12" r="8"/><circle cx="12" cy="12" r="3"/></svg></div><h3>Goal</h3><p>Lorem ipsum dolor sit amet, consectetur adipiscing elit. Ut elit tellus, luctus nec ullamcorper mattis, pulvinar dapibus leo.</p></div>
  <div class="abs btn-gold" style="left:894px;top:1626px;width:148px;height:39px">KNOW MORE &#10148;</div>

  <!-- services -->
  <svg class="abs" style="left:23px;top:1736px" width="1153" height="1120" viewBox="0 0 1153 1120" preserveAspectRatio="none" aria-hidden="true">
    <path d="M0 20 C300 -20 600 60 900 20 S1120 0 1153 60 L1153 1110 C900 1050 650 1080 400 1060 S100 1050 0 1080 Z" fill="#e8ede1"/>
  </svg>
  <div class="abs label" style="top:1756px">Services</div>
  <h2 class="abs title" style="top:1786px">How Can We<br>Help You?</h2>

  <div class="abs card" style="left:163px;top:1893px"><div class="ph" role="img" aria-label="Photo of a hand pressing an alarm keypad" style="background:linear-gradient(135deg,#f2f2f2,#d7d2cc)"></div><h3>Alarm Systems</h3><p>Lorem ipsum dolor sit amet, consectetur adipiscing elit, sed do eiusmod tempor incididunt ut labore et dolore magna aliqua. Ut enim ad minim veniam, quis nostrud exercitation ullamco laboris nisi ut aliquip ex ea commodo consequat.</p><div class="more">READ MORE &#10148;</div></div>
  <div class="abs card" style="left:459px;top:1893px"><div class="ph" role="img" aria-label="Photo of a ceiling dome surveillance camera" style="background:linear-gradient(180deg,#f4f4f4,#cfcfcf)"></div><h3>Video Surveillance</h3><p>Lorem ipsum dolor sit amet, consectetur adipiscing elit, sed do eiusmod tempor incididunt ut labore et dolore magna aliqua. Ut enim ad minim veniam, quis nostrud exercitation ullamco laboris nisi ut aliquip ex ea commodo consequat.</p><div class="more">READ MORE &#10148;</div></div>
  <div class="abs card" style="left:755px;top:1893px"><div class="ph" role="img" aria-label="Photo of a hand holding a key card to an access reader" style="background:linear-gradient(135deg,#ececec,#d8cfc6)"></div><h3>Access Control</h3><p>Lorem ipsum dolor sit amet, consectetur adipiscing elit, sed do eiusmod tempor incididunt ut labore et dolore magna aliqua. Ut enim ad minim veniam, quis nostrud exercitation ullamco laboris nisi ut aliquip ex ea commodo consequat.</p><div class="more">READ MORE &#10148;</div></div>

  <div class="abs card" style="left:163px;top:2328px"><div class="ph" role="img" aria-label="Photo of a smoke detector with smoke" style="background:linear-gradient(180deg,#d9dadb,#f1f1f1)"></div><h3>Fire Alarm</h3><p>Lorem ipsum dolor sit amet, consectetur adipiscing elit, sed do eiusmod tempor incididunt ut labore et dolore magna aliqua. Ut enim ad minim veniam, quis nostrud exercitation ullamco laboris nisi ut aliquip ex ea commodo consequat.</p><div class="more">READ MORE &#10148;</div></div>
  <div class="abs card" style="left:459px;top:2328px"><div class="ph" role="img" aria-label="Photo of a person pressing an intercom button" style="background:linear-gradient(90deg,#e9e9e9,#c99a6c)"></div><h3>Intercom</h3><p>Lorem ipsum dolor sit amet, consectetur adipiscing elit, sed do eiusmod tempor incididunt ut labore et dolore magna aliqua. Ut enim ad minim veniam, quis nostrud exercitation ullamco laboris nisi ut aliquip ex ea commodo consequat.</p><div class="more">READ MORE &#10148;</div></div>
  <div class="abs card" style="left:755px;top:2328px"><div class="ph" role="img" aria-label="Photo of a fingerprint time and attendance terminal" style="background:linear-gradient(180deg,#f5f5f5,#8a8f95)"></div><h3>Time And Attendance</h3><p>Lorem ipsum dolor sit amet, consectetur adipiscing elit, sed do eiusmod tempor incididunt ut labore et dolore magna aliqua. Ut enim ad minim veniam, quis nostrud exercitation ullamco laboris nisi ut aliquip ex ea commodo consequat.</p><div class="more">READ MORE &#10148;</div></div>
  <div class="abs btn-gold" style="left:848px;top:2751px;width:194px;height:39px;background:transparent">CHECK ALL SERVICES &#10148;</div>

  <!-- industries -->
  <div class="abs label" style="top:2932px">Whom We Serve</div>
  <h2 class="abs title" style="top:2964px">Industries<br>We Serve</h2>
  <p class="abs" style="left:0;top:3042px;width:1200px;text-align:center;font-size:11.5px;color:#555">Below are some of the industries we serve. To discuss your particular situation, please contact us.</p>

  <div class="abs ind" style="left:163px;top:3096px"><div class="ph" role="img" aria-label="Photo of a security camera on a dark building facade" style="background:linear-gradient(180deg,#5d6064,#3a3c3f)"></div><div class="cap"><h3>Commercial</h3><p>Lorem ipsum dolor sit amet, consectetur adipiscing elit, sed do eiusmod tempor incididunt ut labore et dolore magna aliqua.</p></div></div>
  <div class="abs ind" style="left:459px;top:3096px"><div class="ph" role="img" aria-label="Photo of students in a classroom" style="background:linear-gradient(135deg,#7a6a5d,#2f3133 60%,#d9d6d2)"></div><div class="cap"><h3>Schools &amp; Educational</h3><p>Lorem ipsum dolor sit amet, consectetur adipiscing elit, sed do eiusmod tempor incididunt ut labore et dolore magna aliqua.</p></div></div>
  <div class="abs ind" style="left:755px;top:3096px"><div class="ph" role="img" aria-label="Photo of hotel staff in a lobby" style="background:linear-gradient(135deg,#b99a6f,#e4ddd2 55%,#6b5440)"></div><div class="cap"><h3>Hotels &amp; Hospitality</h3><p>Lorem ipsum dolor sit amet, consectetur adipiscing elit, sed do eiusmod tempor incididunt ut labore et dolore magna aliqua.</p></div></div>
  <div class="abs btn-gold" style="left:894px;top:3540px;width:148px;height:39px;color:#333">KNOW MORE &#10148;</div>

  <!-- cta -->
  <div class="abs cta" role="img" aria-label="Photo of a wall-mounted security camera"></div>
  <div class="abs cta-gold"></div>
  <h2 class="abs cta-title">Would you like to Secure Your<br>premises?</h2>
  <p class="abs cta-text">Etiam erat lectus, finibus eget commodo quis, tincidunt eget leo. Nullam quis vulputate orci, ac accumsan quam. Morbi fringilla congue libero. Lorem ipsum dolor sit amet, consectetur adipiscing elit, sed do eiusmod tempor incididunt ut labore et dolore magna aliqua.</p>
  <div class="abs cta-btn">&#9990; CALL US NOW<br>603-555-0148</div>

  <!-- testimonial -->
  <div class="abs label" style="top:4028px">Testimony</div>
  <h2 class="abs title" style="top:4056px">What Our<br>Clients Say?</h2>
  <div class="abs testi"></div>
  <div class="abs testi-brand"><span class="dot"></span><span class="name">BEACON RIDGE<br>SECURITY</span></div>
  <p class="abs quote">"Lorem ipsum dolor sit amet, consectetur adipiscing elit, sed do eiusmod tempor incididunt ut labore et dolore magna aliqua. Ut enim ad minim veniam, quis nostrud exercitation ullamco laboris nisi ut aliquip ex ea commodo consequat. "</p>
  <div class="abs testi-line"></div>
  <div class="abs testi-name">Mara Ellison</div>
  <div class="abs testi-role">Firm CEO</div>
  <div class="abs testi-photo" role="img" aria-label="Photo of a businesswoman working at a laptop in an office"></div>

  <!-- footer -->
  <svg class="abs" style="left:23px;top:4620px" width="1153" height="380" viewBox="0 0 1153 380" preserveAspectRatio="none" aria-hidden="true">
    <path d="M0 60 C250 10 450 70 700 40 S1050 0 1153 30 L1153 380 L0 380 Z" fill="#111"/>
  </svg>
  <div class="abs footer-col" style="left:150px;top:4718px;width:180px;text-align:center">
    <div style="display:flex;align-items:center;justify-content:center;gap:8px;margin-bottom:26px"><span style="width:12px;height:12px;border-radius:50%;background:var(--gold)"></span><span style="font-family:Poppins,sans-serif;font-weight:700;font-size:15px;line-height:1.05;color:#fff">BEACON RIDGE<br>SECURITY</span></div>
    <p>Lorem ipsum dolor sit amet, consectetur adipiscing elit. Ut elit tellus, luctus nec ullamcorper mattis, pulvinar dapibus leo.</p>
  </div>
  <div class="abs footer-col" style="left:351px"><h4>Quick Link</h4><ul style="padding-left:14px"><li>Home</li><li>About</li><li>Services</li><li>Contact</li></ul></div>
  <div class="abs footer-col" style="left:532px"><h4>Services</h4><ul class="tight" style="padding-left:14px;line-height:19px"><li>Alarm Systems</li><li>Video Surveillance</li><li>Access Control</li><li>Fire Alarm</li><li>Intercom</li><li>Time And<br>Attendance</li></ul></div>
  <div class="abs footer-col" style="left:712px"><h4>Contact Us</h4><ul style="line-height:18px"><li><span style="color:var(--gold)">&#9679;</span> 48 Harlow Lane<br>&nbsp;&nbsp;&nbsp;&nbsp;Dover, NH 03820</li><li><span style="color:var(--gold)">&#9993;</span> 48 Harlow Lane<br>&nbsp;&nbsp;&nbsp;&nbsp;Dover, NH 03820</li><li><span style="color:var(--gold)">&#9990;</span> 603-555-0148</li></ul></div>
  <div class="abs footer-col" style="left:877px"><h4>Find Us Location Map</h4></div>
  <div class="abs" style="left:877px;top:4740px;width:167px;height:135px;background:linear-gradient(135deg,#e6eee2,#d5e0ea)" role="img" aria-label="Location map of the office"></div>

  <div class="abs copy">Copyright &copy; 2021 BeaconRidgeSecurity | Powered by BeaconRidgeSecurity</div>
</div>
</body>
</html>
```